Icon Selection Project for Graphic Designer

We need a graphic designer to find a series of 6 icons to be used as website navigation/action bar for a website that are redesigning. I am putting details into the attached file.

Target Market(s)

People interested in reading daily inspirational quotes

Requirements
Must have
• White icons that are easy to understand

```html
<!DOCTYPE html>
<html lang="en">
<head>
<meta charset="utf-8">
<title>Lumen Sayings – Navigation</title>
<link href="https://fonts.googleapis.com/css2?family=Inter:wght@300;400;500;700&family=Nunito:wght@500&display=swap" rel="stylesheet">
<style>
  :root {
    --ink: #ffffff;
    --night-top: #2e2340;
    --night-mid: #5a3f5e;
    --dusk: #8e5e66;
    --ember: #c8692f;
    --sand: #6a3a22;
    --panel: #281c33;
    --panel-deep: #231829;
    --icon-fill: rgba(255,255,255,0.45);
  }
  * { box-sizing: border-box; margin: 0; padding: 0; }
  html, body { width: 1200px; height: 1200px; overflow: hidden; background: var(--panel); }
  body { position: relative; font-family: "Inter", Helvetica, Arial, sans-serif; color: var(--ink); }

  .hero {
    position: absolute; left: 0; top: 0; width: 1200px; height: 491px;
    background: linear-gradient(180deg, var(--night-top) 0%, var(--night-mid) 45%, var(--dusk) 72%, var(--ember) 88%, var(--sand) 100%);
  }
  .brand { position: absolute; left: 42px; top: 22px; }
  .brand-name { font-family: "Nunito", sans-serif; font-weight: 500; font-size: 34px; letter-spacing: 0.5px; color: var(--ink); line-height: 1; }
  .brand-tag {
    position: absolute; left: 11px; top: 51px; width: 91px; height: 19px;
    background: #fff; border: 1px solid #999; color: #222;
    font-family: "Nunito", sans-serif; font-size: 11px; line-height: 17px; text-align: center;
  }

  .top-nav { position: absolute; top: 34px; left: 0; width: 1200px; height: 60px; }
  .top-nav .item { position: absolute; width: 90px; margin-left: -45px; text-align: center; }
  .top-nav svg { width: 32px; height: 32px; display: block; margin: 0 auto; }
  .top-nav .label { display: block; margin-top: 9px; font-size: 12px; font-weight: 400; }

  .prev { position: absolute; left: 27px; top: 238px; width: 16px; height: 30px; }

  .quote { position: absolute; left: 0; width: 1200px; text-align: center; }
  .quote-text { top: 220px; font-size: 20px; font-weight: 500; letter-spacing: -0.6px; }
  .quote-author { top: 265px; font-size: 17px; font-weight: 500; }
  .quote-topic { top: 427px; font-size: 20px; font-weight: 700; letter-spacing: -0.5px; }

  .action-panel {
    position: absolute; left: 0; width: 1200px; height: 355px;
    background: radial-gradient(ellipse at 50% 40%, var(--panel) 0%, var(--panel-deep) 100%);
  }
  .panel-one { top: 491px; }
  .panel-two { top: 846px; height: 354px; }
  .action { position: absolute; top: 86px; width: 300px; margin-left: -150px; text-align: center; }
  .action svg { width: 104px; height: 104px; display: block; margin: 0 auto; }
  .action .label { display: block; margin-top: 32px; font-size: 40px; font-weight: 300; line-height: 1.1; }
</style>
</head>
<body>

<svg width="0" height="0" style="position:absolute" aria-hidden="true">
  <defs>
    <symbol id="icon-share" viewBox="0 0 100 100">
      <rect x="30" y="30" width="40" height="40" fill="var(--icon-fill)"/>
      <rect x="6" y="6" width="64" height="64" rx="4" fill="none" stroke="#fff" stroke-width="4"/>
      <rect x="30" y="30" width="64" height="64" rx="4" fill="none" stroke="#fff" stroke-width="4"/>
    </symbol>
    <symbol id="icon-count" viewBox="0 0 100 100">
      <path d="M50 6 A42 42 0 1 1 30 84 L12 94 L18 74 A42 42 0 0 1 50 6 Z" fill="none" stroke="#fff" stroke-width="4" stroke-linejoin="round"/>
      <text x="52" y="64" text-anchor="middle" font-family="Inter, sans-serif" font-weight="300" font-size="42" fill="#fff">5</text>
    </symbol>
    <symbol id="icon-bell" viewBox="0 0 100 100">
      <circle cx="50" cy="50" r="45" fill="none" stroke="#fff" stroke-width="4"/>
      <path d="M50 25 C39 25 35 34 35 45 V58 L29 66 H71 L65 58 V45 C65 34 61 25 50 25 Z" fill="#fff"/>
      <circle cx="50" cy="71" r="6" fill="#fff"/>
    </symbol>
    <symbol id="icon-topics" viewBox="0 0 100 100">
      <path d="M6 10 H62 V50 H26 L12 62 V50 H6 Z" fill="none" stroke="#fff" stroke-width="4" stroke-linejoin="round"/>
      <path d="M38 40 H94 V80 H88 V92 L74 80 H38 Z" fill="#281c33" stroke="#fff" stroke-width="4" stroke-linejoin="round"/>
      <line x1="50" y1="54" x2="82" y2="54" stroke="#fff" stroke-width="4" stroke-linecap="round"/>
      <line x1="50" y1="66" x2="74" y2="66" stroke="#fff" stroke-width="4" stroke-linecap="round"/>
    </symbol>
    <symbol id="icon-random" viewBox="0 0 100 100">
      <rect x="8" y="8" width="84" height="84" rx="14" fill="none" stroke="#fff" stroke-width="4"/>
      <rect x="45" y="24" width="10" height="38" rx="3" fill="#fff"/>
      <circle cx="50" cy="74" r="6" fill="#fff"/>
    </symbol>
    <symbol id="icon-heart" viewBox="0 0 100 100">
      <path d="M50 88 L14 52 C2 40 6 16 26 14 C38 13 46 20 50 28 C54 20 62 13 74 14 C94 16 98 40 86 52 Z" fill="none" stroke="#fff" stroke-width="4" stroke-linejoin="round"/>
    </symbol>
  </defs>
</svg>

<header class="hero" role="img" aria-label="Desert dunes under a starry dusk sky"></header>

<div class="brand">
  <div class="brand-name">Lumen Sayings</div>
  <div class="brand-tag">Lumen Sayings</div>
</div>

<nav class="top-nav" aria-label="Main">
  <div class="item" style="left:696px"><svg><use href="#icon-share"/></svg><span class="label">Share</span></div>
  <div class="item" style="left:793px"><svg><use href="#icon-count"/></svg><span class="label">My Quotes</span></div>
  <div class="item" style="left:887px"><svg><use href="#icon-bell"/></svg><span class="label">Subcribe</span></div>
  <div class="item" style="left:964px"><svg><use href="#icon-topics"/></svg><span class="label">Topics</span></div>
  <div class="item" style="left:1061px"><svg><use href="#icon-random"/></svg><span class="label">Random</span></div>
  <div class="item" style="left:1155px"><svg><use href="#icon-heart"/></svg><span class="label">Favorite</span></div>
</nav>

<svg class="prev" viewBox="0 0 16 30" aria-label="Previous quote">
  <path d="M13 2 L3 15 L13 28" fill="none" stroke="#fff" stroke-width="2" stroke-linecap="round" stroke-linejoin="round"/>
</svg>

<p class="quote quote-text">Faith is composed of the heart's intention. Light comes through faith.</p>
<p class="quote quote-author">Rig Veda</p>
<p class="quote quote-topic">Topic: Gratitude &amp; Faith</p>

<section class="action-panel panel-one">
  <div class="action" style="left:230px"><svg><use href="#icon-share"/></svg><span class="label">Share</span></div>
  <div class="action" style="left:581px"><svg><use href="#icon-count"/></svg><span class="label">My Quotes</span></div>
  <div class="action" style="left:921px"><svg><use href="#icon-bell"/></svg><span class="label">Subcribe</span></div>
</section>

<section class="action-panel panel-two">
  <div class="action" style="left:230px"><svg><use href="#icon-topics"/></svg><span class="label">Topics</span></div>
  <div class="action" style="left:581px"><svg><use href="#icon-random"/></svg><span class="label">Random</span></div>
  <div class="action" style="left:921px"><svg><use href="#icon-heart"/></svg><span class="label">Favorite</span></div>
</section>

</body>
</html>
```